Commercial Janitorial Company needs a Postcard Design

We need a postcard design-i attached a sample-of one-not our industry-but same size and similar to content and what i am looking for-We are a commercial janitorial service-(not residential) we service High Tech-Bio Tech-Manufacturing-Office-Property Management Company'sThe design should incorporate Industry Services-Industries served website-company information-Two sided-color-our website: www.marlowcrestfacilitysvc.com will have information to use-bullet point type-should include Nice artwork-Attention grabbing headline then of course all our contact information found on website

The postcard is NOT a mailer but a hand-out (2 sides)-about 9" Long by 7" wide-

Target Market(s)

Commercial office Building's

Colors

Designer to choose colors to be used in the design.

Requirements
Must have
• All company information-website
• Services offered-Industries served
• Something mentioned about "Green Cleaning"
• Images of cleaning are good-in a commercial setting--Hi Tech-Bio Tech-Cleanroom Cleaning
• 24/7 access
• Locally owned and operated
• 25 Years in business
• Service Excellence
• With our highly-trained, in-house workforce, you can trust that we’ll provide you with services that increase efficiencies and lower your operating expenses—all while maintaining a uniform standard of service excellence.
• Breadth of Services
• We’ll provide you with an unrivaled range of facilities solutions that will keep your properties safe, clean, comfortable and energy efficient.
• Technology-Enabled Workforce
• Your facilities will be serviced with the support of innovative technology solutions that will simplify service delivery and allow for greater transparency.
• Guaranteed Sustainability Solutions
• We’ve got expertise to support all of your sustainability goals, including green cleaning, VORQ support, bundled energy solutions, and more.
• Size of Postcard is 9.5" length x 7" width
Should not have
• No Residential
• No Maid service
• No Cartoon type images
• Strickly commercial cleaning

```html
<!DOCTYPE html>
<html lang="en">
<head>
<meta charset="utf-8">
<title>Marlowcrest Facility Services – Postcard</title>
<link rel="stylesheet" href="https://fonts.googleapis.com/css2?family=Montserrat:ital,wght@0,900;1,800&family=Nunito+Sans:ital,wght@0,400;0,700;0,800;1,400&display=swap">
<style>
  :root {
    --brand-blue: #0b6fbf;
    --brand-blue-deep: #0a5ea6;
    --ink-black: #1a1a1a;
    --paper: #f3f3f3;
    --white: #ffffff;
    --text-blue: #0b62ad;
    --stage: #e4e6ea;
  }
  * { box-sizing: border-box; margin: 0; padding: 0; }
  html, body { width: 1200px; height: 1200px; overflow: hidden; }
  body {
    background: var(--stage);
    font-family: "Nunito Sans", Arial, sans-serif;
    position: relative;
  }
  .postcard {
    position: absolute;
    left: 215px;
    width: 770px;
    height: 566px;
    overflow: hidden;
    background: var(--paper);
    box-shadow: 0 6px 18px rgba(0,0,0,.18);
  }
  .postcard--front { top: 24px; }
  .postcard--back { top: 610px; }

  /* Front */
  .headline-panel {
    position: absolute; left: 0; top: 0; width: 445px; height: 253px;
    background: linear-gradient(135deg, var(--brand-blue) 0%, var(--brand-blue-deep) 100%);
    color: var(--white);
  }
  .headline {
    position: absolute; left: 32px; top: 26px;
    font-family: "Montserrat", Arial, sans-serif; font-weight: 900;
    font-size: 45px; line-height: 50px; letter-spacing: 0.5px;
  }
  .tenure {
    position: absolute; left: 32px; top: 196px;
    font-style: italic; font-size: 19px;
  }
  .services-panel {
    position: absolute; left: 0; top: 253px; width: 445px; height: 313px;
    background: var(--ink-black); color: var(--white);
  }
  .services-title {
    position: absolute; left: 32px; top: 36px;
    font-weight: 700; font-size: 27px;
  }
  .service-list { list-style: none; position: absolute; left: 54px; top: 103px; }
  .service-list li {
    display: flex; align-items: center; gap: 14px;
    font-size: 20px; height: 44.5px;
  }
  .service-list svg { width: 28px; height: 26px; flex: none; }
  .intro-panel {
    position: absolute; left: 445px; top: 0; width: 325px; height: 253px;
    background: var(--paper);
  }
  .company-mark {
    position: absolute; left: 0; right: 0; top: 42px;
    display: flex; justify-content: center; align-items: center; gap: 8px;
    font-weight: 800; font-size: 24px; color: var(--brand-blue);
  }
  .company-mark .square { width: 18px; height: 18px; background: var(--brand-blue); }
  .company-sub {
    position: absolute; left: 0; right: 0; top: 78px; text-align: center;
    font-weight: 800; font-size: 10px; letter-spacing: .5px; color: var(--ink-black);
  }
  .intro-text {
    position: absolute; left: 32px; top: 125px; width: 275px;
    font-size: 12.4px; line-height: 18.8px; color: var(--text-blue);
  }
  .intro-text strong { font-weight: 800; }
  .call-line {
    position: absolute; left: 70px; top: 220px;
    font-family: "Montserrat", Arial, sans-serif; font-style: italic; font-weight: 800;
    font-size: 17px; color: var(--ink-black);
  }
  .photo { position: absolute; top: 253px; height: 313px; }
  .photo--crew {
    left: 445px; width: 161px;
    background: linear-gradient(160deg, #b9a58b 0%, #2f4160 55%, #e3c63a 100%);
  }
  .photo--cleaner {
    left: 607px; width: 163px;
    background: linear-gradient(170deg, #e8e6e1 0%, #c9a98d 40%, #4d6ea6 75%, #2d7fd0 100%);
  }
  .access-badge {
    position: absolute; left: 390px; top: 200px; width: 108px; height: 108px;
  }

  /* Back */
  .values-panel {
    position: absolute; left: 0; top: 0; width: 312px; height: 566px;
    background: linear-gradient(160deg, var(--brand-blue) 0%, var(--brand-blue-deep) 100%);
    color: var(--white);
  }
  .value-list { list-style: none; position: absolute; left: 54px; top: 62px; }
  .value-list li {
    display: flex; align-items: center; gap: 10px;
    font-size: 18px; height: 84px;
  }
  .value-list li::before {
    content: ""; width: 10px; height: 10px; border-radius: 50%;
    background: var(--ink-black); flex: none;
  }
  .value-list strong { font-weight: 800; }
  .benefits {
    position: absolute; left: 346px; top: 43px; width: 392px;
    color: var(--text-blue); font-size: 12.2px; line-height: 18.8px;
  }
  .benefits p { margin-bottom: 18.8px; }
</style>
</head>
<body>

<section class="postcard postcard--front">
  <div class="headline-panel">
    <h1 class="headline">EFFECTIVE<br>COMMERCIAL<br>CLEANING</h1>
    <p class="tenure">25 Years in business</p>
  </div>

  <div class="services-panel">
    <h2 class="services-title">Our Services</h2>
    <ul class="service-list">
      <li><svg viewBox="0 0 28 26"><path d="M2 14 L10 22 L26 3" fill="none" stroke="#1c7fd6" stroke-width="5" stroke-linecap="round" stroke-linejoin="round"/></svg>Janitorial Services</li>
      <li><svg viewBox="0 0 28 26"><path d="M2 14 L10 22 L26 3" fill="none" stroke="#1c7fd6" stroke-width="5" stroke-linecap="round" stroke-linejoin="round"/></svg>Green Cleaning</li>
      <li><svg viewBox="0 0 28 26"><path d="M2 14 L10 22 L26 3" fill="none" stroke="#1c7fd6" stroke-width="5" stroke-linecap="round" stroke-linejoin="round"/></svg>Recycling</li>
      <li><svg viewBox="0 0 28 26"><path d="M2 14 L10 22 L26 3" fill="none" stroke="#1c7fd6" stroke-width="5" stroke-linecap="round" stroke-linejoin="round"/></svg>Cleanroom Cleaning</li>
    </ul>
  </div>

  <div class="intro-panel">
    <div class="company-mark"><span class="square"></span>Marlowcrest</div>
    <div class="company-sub">FACILITY SERVICES INC.</div>
    <p class="intro-text"><strong>Marlowcrest</strong> formed as it became increasingly clear that companies in the Bay Area needed a reliable, professional, multi-faceted building maintenance contractor to service their building maintenance needs.</p>
    <p class="call-line">CALL: 408-555-0192</p>
  </div>

  <div class="photo photo--crew" role="img" aria-label="Masked cleaning worker mopping a warehouse floor beside a yellow bucket"></div>
  <div class="photo photo--cleaner" role="img" aria-label="Smiling cleaner in checked shirt giving a thumbs up, holding a bucket of supplies"></div>

  <svg class="access-badge" viewBox="0 0 108 108" aria-label="24/7 access">
    <polygon fill="#0b6fbf" points="54,2 63,30 88,14 79,41 106,44 82,58 100,80 72,75 70,104 54,82 38,104 36,75 8,80 26,58 2,44 29,41 20,14 45,30"/>
    <g transform="rotate(-18 54 54)" fill="#fff" text-anchor="middle" font-family="Montserrat, Arial, sans-serif">
      <text x="56" y="56" font-size="22" font-weight="900" font-style="italic">24/7</text>
      <text x="56" y="72" font-size="13" font-weight="800" font-style="italic">access</text>
    </g>
  </svg>
</section>

<section class="postcard postcard--back">
  <div class="values-panel">
    <ul class="value-list">
      <li><span>We Value <strong>CUSTOMERS</strong></span></li>
      <li><span>We Value <strong>EXECUTION</strong></span></li>
      <li><span>We Value <strong>INTEGRITY</strong></span></li>
      <li><span>We Value <strong>INNOVATION</strong></span></li>
      <li><span>We Value <strong>TEAMWORK</strong></span></li>
      <li><span>We Value <strong>RESULTS</strong></span></li>
    </ul>
  </div>

  <div class="benefits">
    <p>- With our highly-trained, in-house workforce, you can trust that we’ll provide you with services that increase efficiencies and lower your operating expenses—all while maintaining a uniform standard of service excellence.</p>
    <p>- Breadth of Services</p>
    <p>- We’ll provide you with an unrivaled range of facilities solutions that will keep your properties safe, clean, comfortable and energy efficient.</p>
    <p>- We’ll provide you with an unrivaled range of facilities solutions that will keep your properties safe, clean, comfortable and energy efficient.</p>
    <p>- Technology-Enabled Workforce</p>
    <p>- Your facilities will be serviced with the support of innovative technology solutions that will simplify service delivery and allow for greater transparency.</p>
    <p>- Guaranteed Sustainability Solutions</p>
    <p>- We’ve got expertise to support all of your sustainability goals, including green cleaning, VORQ support, bundled energy solutions, and more.</p>
  </div>
</section>

</body>
</html>
```